Personal Business Card Design Project

I require a two sided personal business card design.

I am a 35 year old Angel Investor and I invest in various niche internet and F&B projects in China. I am Chinese Australian

One side should be in English and the other side should be in Chinese.

My English details are:

Cole Marsh
Angel Investor

China: +86 1390 274 5183
Hong Kong: +852 6133 4087
Email: cole@cdmarsh.net
Address: Flat 2407, Block 5, Pinecrest Gardens,
42 Maoyuan Road (near Beiling Road),
Shanghai, 200437,
China

My Chinese details are (do not print the text in brackets)

袁哲明 (Name)
天使投资者(Angel Investor)

中国 (China): +86 1390 274 5183
香港 (Hong Kong): +852 6133 4087
Email: cole@cdmarsh.net
地址 (Address): 上海市茂园路42号5号楼2407室
松岭花园, 中国 200437

Target Market(s)

I will only give this card to present to new partners and suppliers and people asking for funding. Not customers.

Industry/Entity Type

Internet

Requirements
Must have
• Something a little humourous in terms of graphics that suggest helping something to grow since I invest in startups. But I want a sophisticated look to it as well.
Nice to have
• Black and White tongue in cheek graphics but not overboard.

The whole card can be not conventional in shape or have cutouts but still retain the business standard business card size.

```html
<!DOCTYPE html>
<html lang="en">
<head>
<meta charset="utf-8">
<title>Cole Marsh · Business Card</title>
<link rel="stylesheet" href="https://fonts.googleapis.com/css2?family=Questrial&family=Noto+Sans+SC:wght@300;400&display=swap">
<style>
  :root {
    --backdrop: #ecebe8;
    --card: #f4f4f3;
    --ink: #1a1a1a;
    --band-black: #0c0c0c;
    --on-gold: #ffffff;
    --graphic: #e7e7e6;
    --card-shadow: rgba(0,0,0,0.18);
  }
  * { margin: 0; padding: 0; box-sizing: border-box; }
  html, body { width: 1200px; height: 900px; overflow: hidden; }
  body {
    background: var(--backdrop);
    font-family: "Questrial", "Noto Sans SC", sans-serif;
    color: var(--ink);
    position: relative;
  }
  .card {
    position: absolute;
    top: 300px;
    width: 520px;
    height: 300px;
    background: var(--card);
    box-shadow: 0 6px 18px var(--card-shadow);
    overflow: hidden;
  }
  .card--chinese { left: 50px; font-family: "Noto Sans SC", "Questrial", sans-serif; }
  .card--english { left: 630px; }
  .card__art { position: absolute; inset: 0; width: 520px; height: 300px; }
  .card__graphic {
    position: absolute; left: 330px; top: 100px; width: 150px; height: 150px;
    background: radial-gradient(circle, var(--graphic) 0%, rgba(231,231,230,0) 70%);
  }
  .card__name {
    position: absolute; left: 24px; top: 30px;
    font-size: 34px; font-weight: 400; color: var(--on-gold);
    letter-spacing: 1px; line-height: 1;
  }
  .card--chinese .card__name { font-weight: 300; font-size: 34px; letter-spacing: 3px; }
  .card__title {
    position: absolute; right: 34px; top: 20px;
    font-size: 15px; color: var(--on-gold); line-height: 1;
  }
  .card__text {
    position: absolute; font-size: 11.5px; line-height: 14px; white-space: nowrap;
  }
  .card__label { left: 28px; }
  .card__colon { left: 124px; }
  .card__value { left: 172px; }
  .card--chinese .card__address { font-size: 12.5px; line-height: 16px; }
</style>
</head>
<body>

<svg width="0" height="0" style="position:absolute" aria-hidden="true">
  <defs>
    <linearGradient id="gold" x1="0" y1="0" x2="1" y2="0">
      <stop offset="0" stop-color="#e3b70f"/>
      <stop offset="1" stop-color="#e39a10"/>
    </linearGradient>
  </defs>
</svg>

<!-- Chinese side -->
<article class="card card--chinese" lang="zh">
  <div class="card__graphic" role="img" aria-label="Faint growth graphic"></div>
  <svg class="card__art" viewBox="0 0 520 300" aria-hidden="true">
    <rect x="0" y="0" width="520" height="78" fill="url(#gold)"/>
    <rect x="0" y="78" width="520" height="10" fill="var(--band-black)"/>
    <polygon points="246,0 262,0 250,88 234,88" fill="var(--card)"/>
    <rect x="0" y="258" width="520" height="14" fill="var(--band-black)"/>
  </svg>
  <h1 class="card__name">袁哲明</h1>
  <p class="card__title">天使投资者</p>

  <p class="card__text card__value" style="top:106px">+86 1390 274 5183<br>+852 6133 4087</p>
  <p class="card__text card__label" style="top:124px">中国<br>香港</p>
  <p class="card__text card__colon" style="top:124px">:<br>:</p>
  <p class="card__text card__value" style="top:148px">cole@cdmarsh.net</p>
  <p class="card__text card__label" style="top:168px">Email</p>
  <p class="card__text card__colon" style="top:168px">:</p>
  <p class="card__text card__value card__address" style="top:170px">上海市茂园路42号5号楼2407室<br>松岭花园, 中国 200437</p>
  <p class="card__text card__label" style="top:196px">地址</p>
  <p class="card__text card__colon" style="top:196px">:</p>
</article>

<!-- English side -->
<article class="card card--english" lang="en">
  <div class="card__graphic" role="img" aria-label="Faint growth graphic"></div>
  <svg class="card__art" viewBox="0 0 520 300" aria-hidden="true">
    <rect x="0" y="0" width="520" height="78" fill="url(#gold)"/>
    <rect x="0" y="78" width="520" height="10" fill="var(--band-black)"/>
    <polygon points="226,0 242,0 230,88 214,88" fill="var(--card)"/>
    <rect x="0" y="258" width="520" height="14" fill="var(--band-black)"/>
  </svg>
  <h1 class="card__name">Cole Marsh</h1>
  <p class="card__title">Angel Investor</p>

  <p class="card__text card__value" style="top:104px">+86 1390 274 5183<br>+852 6133 4087</p>
  <p class="card__text card__label" style="top:118px">China<br>Hong Kong</p>
  <p class="card__text card__colon" style="top:118px">:<br>:</p>
  <p class="card__text card__value" style="top:142px">cole@cdmarsh.net</p>
  <p class="card__text card__label" style="top:158px">Email</p>
  <p class="card__text card__colon" style="top:158px">:</p>
  <p class="card__text card__value" style="top:162px">Flat 2407, Block 5, Pinecrest Gardens,<br>42 Maoyuan Road (near Beiling Road),<br>Shanghai, 200437,<br>China</p>
  <p class="card__text card__label" style="top:180px">Address</p>
  <p class="card__text card__colon" style="top:180px">:</p>
</article>

</body>
</html>
```